Travel Consultant Business Card

Hello.. New travel consultant looking seeking a business card that incorporates my new logo. I specialize in cruises but also want to imply land vacation. I am very open to any design and font concepts. I'm looking for a very upbeat modern design that reflects cruise and land vacations. Bright vibrant colors

Target Market(s)

Cruise and Land Vacationers

Industry/Entity Type

Travel Agent

Contact Information for Business Card

I am very open to any design and font concepts. I'm looking for a very upbeat modern design that reflects cruise and land vacations. Bright vibrant colors

Colors

Designer to choose colors to be used in the design.

Requirements
Must have
• Company Name: MapleRidge Journeys---New logo uploaded to be included in design
• My Name: Dolores Kwiatek-Travel Consultant
• Phone Number: (555) 418-7093
• E-Mail Address: mapleridgejourneys@examplemail.net
• Website: www.mapleridgejourneys.example
Nice to have
• My tag line is …..Here to Get You There

```html
<!DOCTYPE html>
<html lang="en">
<head>
<meta charset="utf-8">
<title>MapleRidge Journeys – Business Card</title>
<link rel="stylesheet" href="https://fonts.googleapis.com/css2?family=Andika:wght@400;700&family=Zilla+Slab:wght@400&display=swap">
<style>
  :root {
    --canvas: #ffffff;
    --ocean-light: #8fc3e6;
    --ocean-mid: #2f77bf;
    --ocean-deep: #1b4f9a;
    --forest: #3f7d32;
    --forest-dark: #2c5f26;
    --panel: #ffffff;
    --brand-blue: #1c5ea8;
    --sky-blue: #2fa7e0;
    --leaf-green: #5bb83a;
    --lime-text: #7ab82c;
  }
  * { margin: 0; padding: 0; box-sizing: border-box; }
  html, body { width: 1200px; height: 1000px; overflow: hidden; background: var(--canvas); }
  .canvas { position: relative; width: 1200px; height: 1000px; }

  .card { position: absolute; top: 68px; width: 542px; height: 300px; }
  .card--front { left: 35px; }
  .card--back { left: 622px; }

  .card__frame { position: absolute; inset: 0; width: 542px; height: 300px; display: block; }

  .card__panel {
    position: absolute; left: 43px; top: 43px; width: 456px; height: 215px;
    background: var(--panel);
  }

  .brand-name {
    position: absolute; left: 0; right: 0; top: 82px;
    text-align: center;
    font-family: "Andika", sans-serif; font-weight: 700;
    font-size: 40px; line-height: 1; color: var(--brand-blue);
  }

  .consultant-name {
    position: absolute; left: 32px; top: 28px;
    font-family: "Andika", sans-serif; font-weight: 700;
    font-size: 28px; line-height: 1; color: var(--brand-blue);
  }
  .consultant-role {
    position: absolute; left: 33px; top: 61px;
    font-family: "Zilla Slab", serif; font-size: 18px; letter-spacing: 1.2px;
    line-height: 1; color: var(--sky-blue);
  }
  .divider {
    position: absolute; right: 34px; top: 103px; width: 81px; height: 3px;
    background: var(--leaf-green);
  }
  .contact-list {
    position: absolute; right: 34px; top: 120px; list-style: none; text-align: right;
    font-family: "Andika", sans-serif; font-size: 18px; line-height: 23px; color: var(--lime-text);
  }
</style>
</head>
<body>
<main class="canvas">

  <section class="card card--front" aria-label="Card front">
    <svg class="card__frame" viewBox="0 0 542 300" role="img" aria-label="Photo border: ocean wave at top and left, evergreen forest at right and bottom">
      <defs>
        <linearGradient id="wave-top" x1="0" y1="0" x2="1" y2="0">
          <stop offset="0" stop-color="var(--ocean-mid)"/>
          <stop offset="1" stop-color="var(--ocean-light)"/>
        </linearGradient>
        <linearGradient id="wave-side" x1="0" y1="0" x2="0" y2="1">
          <stop offset="0" stop-color="var(--ocean-mid)"/>
          <stop offset="1" stop-color="var(--ocean-deep)"/>
        </linearGradient>
      </defs>
      <polygon points="0,0 542,0 499,43 43,43" fill="url(#wave-top)"/>
      <polygon points="0,0 43,43 43,258 0,300" fill="url(#wave-side)"/>
      <polygon points="542,0 542,300 499,258 499,43" fill="var(--forest)"/>
      <polygon points="0,300 43,258 499,258 542,300" fill="var(--forest-dark)"/>
    </svg>
    <div class="card__panel">
      <p class="brand-name">MapleRidge Journeys</p>
    </div>
  </section>

  <section class="card card--back" aria-label="Card back">
    <svg class="card__frame" viewBox="0 0 542 300" role="img" aria-label="Photo border: ocean wave at top and left, evergreen forest at right and bottom">
      <defs>
        <linearGradient id="wave-top-b" x1="0" y1="0" x2="1" y2="0">
          <stop offset="0" stop-color="var(--ocean-mid)"/>
          <stop offset="1" stop-color="var(--ocean-light)"/>
        </linearGradient>
        <linearGradient id="wave-side-b" x1="0" y1="0" x2="0" y2="1">
          <stop offset="0" stop-color="var(--ocean-mid)"/>
          <stop offset="1" stop-color="var(--ocean-deep)"/>
        </linearGradient>
      </defs>
      <polygon points="0,0 542,0 499,43 43,43" fill="url(#wave-top-b)"/>
      <polygon points="0,0 43,43 43,258 0,300" fill="url(#wave-side-b)"/>
      <polygon points="542,0 542,300 499,258 499,43" fill="var(--forest)"/>
      <polygon points="0,300 43,258 499,258 542,300" fill="var(--forest-dark)"/>
    </svg>
    <div class="card__panel">
      <h1 class="consultant-name">Dolores Kwiatek</h1>
      <p class="consultant-role">Travel Consultant</p>
      <div class="divider"></div>
      <ul class="contact-list">
        <li>(555) 418-7093</li>
        <li>mapleridgejourneys@examplemail.net</li>
        <li>www.mapleridgejourneys.example</li>
      </ul>
    </div>
  </section>

</main>
</body>
</html>
```